Swimming Pool Business Billboard

10' x 24' Billboard displaying company name, logo and phone number. Picture of swimming pool activity; kids playing , swimming, etc. Bullet points possibly shown: New Construction, Repairs, Weekly maintenance.

Industry/Entity Type

Swimming pool construction, repairs and maintenance.

Font styles to use
Sans Serif

Colors
0054AA
0677BA
7BADD7
CADEEF
E8F1F8

Requirements
Must have
• Benny & Carson Pelletier, BENNY'S POOLS & Service,
Nice to have
• Prefer to have my last name "Pelletier" above the word "POOLS" only in smaller print so that "BENNYS POOLS" is distinguished.

```html
<!DOCTYPE html>
<html lang="en">
<head>
<meta charset="utf-8">
<title>Benny's Pools &amp; Service Billboard</title>
<link href="https://fonts.googleapis.com/css2?family=Alfa+Slab+One&family=Roboto+Slab:wght@800&family=Arimo:wght@700&display=swap" rel="stylesheet">
<style>
  :root {
    --pool-cyan: #2dbcd4;
    --pool-cyan-deep: #22afca;
    --pool-light: #5fd0e2;
    --cream: #f0dc9b;
    --white: #ffffff;
    --float-yellow: #f4e49a;
    --float-pink: #e2b6df;
    --float-aqua: #9fdbe6;
    --float-green: #c9e39a;
    --swimsuit-blue: #a9d8e4;
  }
  html, body {
    margin: 0;
    padding: 0;
    width: 1200px;
    height: 500px;
    overflow: hidden;
    background: var(--pool-cyan);
  }
  .billboard {
    position: relative;
    width: 1200px;
    height: 500px;
    overflow: hidden;
    background: linear-gradient(90deg, var(--pool-cyan) 0%, var(--pool-cyan) 60%, var(--pool-cyan-deep) 100%);
  }
  .pool-photo {
    position: absolute;
    left: 640px;
    top: 0;
    width: 560px;
    height: 500px;
  }
  .brand-badge {
    position: absolute;
    left: 40px;
    top: 53px;
    width: 134px;
    height: 134px;
    border-radius: 50%;
    background: var(--white);
    display: flex;
    align-items: center;
    justify-content: center;
    text-align: center;
    font-family: "Roboto Slab", serif;
    font-weight: 800;
    font-size: 17px;
    line-height: 1.15;
    color: var(--pool-cyan-deep);
  }
  .owner-name {
    position: absolute;
    left: 188px;
    top: 68px;
    margin: 0;
    font-family: "Roboto Slab", serif;
    font-weight: 800;
    font-size: 32px;
    line-height: 1;
    color: var(--white);
    white-space: nowrap;
  }
  .company-name {
    position: absolute;
    left: 186px;
    top: 118px;
    margin: 0;
    font-family: "Alfa Slab One", serif;
    font-weight: 400;
    font-size: 74px;
    line-height: 76px;
    color: var(--cream);
    letter-spacing: 1px;
  }
  .company-name span { display: block; }
  .phone {
    position: absolute;
    left: 192px;
    top: 350px;
    margin: 0;
    font-family: "Arimo", sans-serif;
    font-weight: 700;
    font-size: 44px;
    line-height: 1;
    color: var(--white);
    white-space: nowrap;
  }
  .services {
    position: absolute;
    left: 193px;
    top: 437px;
    margin: 0;
    padding: 0;
    list-style: none;
    display: flex;
    font-family: "Roboto Slab", serif;
    font-weight: 800;
    font-size: 14px;
    letter-spacing: 2.2px;
    line-height: 1;
    color: var(--cream);
    white-space: nowrap;
  }
  .services li + li::before {
    content: "|";
    margin: 0 20px;
  }
</style>
</head>
<body>
  <div class="billboard">
    <svg class="pool-photo" role="img" aria-label="Photo of a child in a swimsuit relaxing on a colorful inflatable pool ring, floating in bright blue pool water" viewBox="0 0 560 500">
      <defs>
        <linearGradient id="water" x1="0" y1="0" x2="1" y2="1">
          <stop offset="0" stop-color="#2dbcd4"/>
          <stop offset="1" stop-color="#3cc6dc"/>
        </linearGradient>
        <linearGradient id="floatTones" x1="0" y1="0" x2="0.3" y2="1">
          <stop offset="0" stop-color="var(--float-yellow)"/>
          <stop offset="0.45" stop-color="var(--float-green)"/>
          <stop offset="0.7" stop-color="var(--float-aqua)"/>
          <stop offset="1" stop-color="var(--float-pink)"/>
        </linearGradient>
      </defs>
      <rect width="560" height="500" fill="url(#water)"/>
      <ellipse cx="264" cy="252" rx="230" ry="215" fill="url(#floatTones)"/>
    </svg>

    <div class="brand-badge">BENNY'S<br>POOLS</div>

    <p class="owner-name">Benny &amp; Carson Pelletier</p>

    <h1 class="company-name">
      <span>BENNY’S</span>
      <span>POOLS</span>
      <span>&amp; SERVICE</span>
    </h1>

    <p class="phone">Call : 912-555-0148</p>

    <ul class="services">
      <li>NEW CONSTRUCTION</li>
      <li>REPAIRS</li>
      <li>WEEKLY MAINTENANCE</li>
    </ul>
  </div>
</body>
</html>
```